Maple Ridge business card design

Card needs to include the following text/items:
Company Logo
Tobin Marsh
Phone # - 555-318-7642
service@mapleridgelandscaping.example
Lawn & landscape maintenance services

```html
<!DOCTYPE html>
<html lang="en">
<head>
<meta charset="utf-8">
<title>Maple Ridge Landscaping — Business Card</title>
<link rel="stylesheet" href="https://fonts.googleapis.com/css2?family=Archivo:wght@400;700&display=swap">
<style>
  :root {
    --backdrop: #ababab;
    --card: #e6e7e9;
    --card-edge: #eeeff0;
    --brand-green: #1f4f2a;
    --leaf-green: #7f9c33;
    --ink: #1b1b1b;
    --rule: #6d6d6d;
    --watermark: #dadcdc;
  }
  * { box-sizing: border-box; margin: 0; padding: 0; }
  html, body {
    width: 672px;
    height: 1200px;
    overflow: hidden;
    background: var(--backdrop);
    font-family: "Archivo", "Helvetica Neue", Arial, sans-serif;
  }
  .sheet {
    position: relative;
    width: 672px;
    height: 1200px;
  }
  .card {
    position: absolute;
    left: 106px;
    width: 460px;
    height: 262px;
    background: linear-gradient(120deg, var(--card) 0%, var(--card-edge) 60%, var(--card) 100%);
    overflow: hidden;
  }
  .card--front { top: 300px; }
  .card--back  { top: 630px; }

  /* Front */
  .brand {
    position: absolute;
    inset: 0;
    display: flex;
    flex-direction: column;
    align-items: center;
    justify-content: center;
    gap: 14px;
  }
  .brand__disc {
    width: 112px;
    height: 112px;
    border-radius: 50%;
    background: var(--brand-green);
  }
  .brand__name {
    font-weight: 700;
    font-size: 34px;
    letter-spacing: -0.5px;
    color: var(--brand-green);
  }

  /* Back */
  .watermark {
    position: absolute;
    left: 196px;
    top: 6px;
    width: 290px;
    height: 290px;
    border-radius: 50%;
    background: var(--watermark);
    opacity: 0.6;
  }
  .contact {
    position: absolute;
    inset: 0;
    display: flex;
    flex-direction: column;
    align-items: center;
    padding-top: 60px;
  }
  .contact__name {
    font-weight: 700;
    font-size: 21px;
    letter-spacing: -0.8px;
    color: var(--leaf-green);
  }
  .contact__rule {
    width: 142px;
    height: 1px;
    background: var(--rule);
    margin: 6px 0 6px;
  }
  .contact__role {
    font-size: 14.5px;
    line-height: 14px;
    letter-spacing: -0.6px;
    text-align: center;
    color: var(--ink);
  }
  .contact__lines {
    margin-top: 24px;
    display: flex;
    flex-direction: column;
    align-items: center;
    gap: 7px;
    font-size: 9.5px;
    letter-spacing: -0.4px;
    color: var(--ink);
  }
  .contact__row { display: flex; gap: 12px; }
  .contact__item { display: flex; align-items: center; gap: 5px; }
  .icon { width: 9px; height: 9px; fill: var(--leaf-green); }
</style>
</head>
<body>
<main class="sheet">
  <section class="card card--front" aria-label="Card front">
    <div class="brand">
      <div class="brand__disc" aria-hidden="true"></div>
      <div class="brand__name">Maple Ridge</div>
    </div>
  </section>

  <section class="card card--back" aria-label="Card back">
    <div class="watermark" aria-hidden="true"></div>
    <div class="contact">
      <div class="contact__name">Tobin Marsh</div>
      <div class="contact__rule"></div>
      <div class="contact__role">Lawn &amp; Landscape<br>Maintenance Services</div>
      <div class="contact__lines">
        <div class="contact__row">
          <span class="contact__item">
            <svg class="icon" viewBox="0 0 24 24" aria-hidden="true"><path d="M6.6 10.8a15 15 0 0 0 6.6 6.6l2.2-2.2a1 1 0 0 1 1-.25 11.4 11.4 0 0 0 3.6.57 1 1 0 0 1 1 1V20a1 1 0 0 1-1 1A17 17 0 0 1 3 4a1 1 0 0 1 1-1h3.5a1 1 0 0 1 1 1c0 1.25.2 2.45.57 3.57a1 1 0 0 1-.25 1z"/></svg>
            555-318-7642
          </span>
          <span class="contact__item">
            <svg class="icon" viewBox="0 0 24 24" aria-hidden="true"><circle cx="12" cy="12" r="10"/></svg>
            mapleridgelandscaping.example
          </span>
        </div>
        <span class="contact__item">
          <svg class="icon" viewBox="0 0 24 24" aria-hidden="true"><path d="M2 5h20v14H2z M2 5l10 8 10-8" /></svg>
          service@mapleridgelandscaping.example
        </span>
      </div>
    </div>
  </section>
</main>
</body>
</html>
```